The Larchmont Fitters

We need a business card design for our wardrobe company.
Please visit our website www.glimmerbayinteriors.com to get an idea of who we are.

```html
<!DOCTYPE html>
<html lang="en">
<head>
<meta charset="utf-8">
<title>The Larchmont Fitters — Business Card</title>
<link href="https://fonts.googleapis.com/css2?family=Roboto:wght@400;500;700&display=swap" rel="stylesheet">
<style>
  :root {
    --backdrop: #3a3f45;
    --card: #f4f3f1;
    --ink: #1e1e1e;
    --ink-soft: #4a4a4a;
    --muted: #9a9a9a;
    --rule: #2a2a2a;
  }
  html, body {
    margin: 0;
    padding: 0;
    width: 1200px;
    height: 802px;
    overflow: hidden;
    background: var(--backdrop);
    font-family: "Roboto", Arial, sans-serif;
  }
  .card {
    position: absolute;
    left: 75px;
    top: 101px;
    width: 1050px;
    height: 600px;
    background: var(--card);
    box-shadow: 0 14px 40px rgba(0,0,0,0.35);
    color: var(--ink);
  }
  .person {
    position: absolute;
    left: 110px;
    top: 78px;
  }
  .person__name {
    margin: 0;
    font-size: 44px;
    font-weight: 700;
    letter-spacing: 0.3px;
    line-height: 1;
  }
  .person__role {
    margin: 6px 0 0;
    font-size: 24px;
    font-weight: 400;
    color: var(--muted);
  }
  .rule {
    position: absolute;
    left: 110px;
    width: 220px;
    height: 2px;
    background: var(--rule);
  }
  .rule--top { top: 190px; }
  .rule--bottom { top: 322px; }
  .address {
    position: absolute;
    left: 110px;
    top: 222px;
    margin: 0;
    font-style: normal;
    font-size: 25px;
    line-height: 34px;
    color: var(--ink-soft);
  }
  .contacts {
    position: absolute;
    left: 96px;
    top: 352px;
    margin: 0;
    padding: 0;
    list-style: none;
  }
  .contacts__item {
    display: flex;
    align-items: center;
    gap: 12px;
    font-size: 26px;
    line-height: 38px;
    color: var(--ink-soft);
  }
  .contacts__icon {
    width: 20px;
    height: 20px;
    flex: none;
  }
  .brand {
    position: absolute;
    left: 600px;
    top: 440px;
    display: flex;
    align-items: center;
    gap: 20px;
  }
  .brand__mark {
    width: 54px;
    height: 54px;
    background: var(--ink);
    flex: none;
  }
  .brand__name {
    margin: 0;
    font-size: 25px;
    font-weight: 500;
    letter-spacing: 0.6px;
    text-transform: uppercase;
    color: var(--ink);
  }
  .brand__tagline {
    margin: 6px 0 0 14px;
    font-size: 20px;
    font-weight: 500;
    color: var(--ink);
  }
</style>
</head>
<body>
  <section class="card" aria-label="Business card">
    <div class="person">
      <h1 class="person__name">Daniel Hartley</h1>
      <p class="person__role">President</p>
    </div>

    <div class="rule rule--top"></div>
    <address class="address">Orchard Yard, 42 Fenwick Lane,<br>London EC2R 7QP</address>
    <div class="rule rule--bottom"></div>

    <ul class="contacts">
      <li class="contacts__item">
        <svg class="contacts__icon" viewBox="0 0 20 20" aria-hidden="true">
          <path d="M5 2 L8 6 L6.5 8 Q8 12 12 13.5 L14 12 L18 15 L16 18 Q8 18 3 11 Q1.5 6 5 2 Z" fill="#1e1e1e"/>
        </svg>
        <span>020 7946 0381</span>
      </li>
      <li class="contacts__item">
        <svg class="contacts__icon" viewBox="0 0 20 20" aria-hidden="true">
          <rect x="1" y="4" width="18" height="12" fill="#1e1e1e"/>
          <path d="M1.5 4.5 L10 11 L18.5 4.5" fill="none" stroke="#f4f3f1" stroke-width="1.4"/>
        </svg>
        <span>info@glimmerbayinteriors.com</span>
      </li>
      <li class="contacts__item">
        <svg class="contacts__icon" viewBox="0 0 20 20" aria-hidden="true">
          <circle cx="10" cy="10" r="8.5" fill="#1e1e1e"/>
          <ellipse cx="10" cy="10" rx="3.5" ry="8.5" fill="none" stroke="#f4f3f1" stroke-width="1.1"/>
          <line x1="1.5" y1="10" x2="18.5" y2="10" stroke="#f4f3f1" stroke-width="1.1"/>
        </svg>
        <span>www.glimmerbayinteriors.com</span>
      </li>
    </ul>

    <div class="brand">
      <div class="brand__mark" aria-hidden="true"></div>
      <div class="brand__text">
        <p class="brand__name">The Larchmont Fitters</p>
        <p class="brand__tagline">Measured Right, Built to Last</p>
      </div>
    </div>
  </section>
</body>
</html>
```